Letterhead design for business

Looking for an attractive and professional letterhead that uses the logo that is attached below.

Target Market(s)

Potential bankruptcy clients.

Industry/Entity Type

Legal

Colors

Designer to choose colors to be used in the design.

Requirements
Must have
• Address for locations, phone number, and website address.
• Addresses are on website ferncoveadvice.example. Use following phone number (for tracking purposes): 555-013-8274

```html
<!DOCTYPE html>
<html lang="en">
<head>
<meta charset="utf-8">
<title>Ferncove Legal Letterhead</title>
<link href="https://fonts.googleapis.com/css2?family=Raleway:wght@300;500&display=swap" rel="stylesheet">
<style>
  :root {
    --backdrop: #c2c1c1;
    --paper: #ffffff;
    --brand-green: #7cbf6e;
    --ink-dark: #4a4a4a;
    --ink-body: #3d3d3d;
    --rule: #8a8a8a;
  }
  * { margin: 0; padding: 0; box-sizing: border-box; }
  html, body {
    width: 1200px;
    height: 1200px;
    overflow: hidden;
    background: var(--backdrop);
    font-family: "Raleway", sans-serif;
  }
  .letterhead {
    position: absolute;
    left: 213px;
    top: 100px;
    width: 774px;
    height: 1000px;
    background: var(--paper);
  }
  .brand {
    position: absolute;
    top: 46px;
    left: 0;
    width: 100%;
    display: flex;
    flex-direction: column;
    align-items: center;
  }
  .brand-mark {
    width: 56px;
    height: 56px;
    border-radius: 50%;
    background: var(--brand-green);
    margin-bottom: 12px;
  }
  .brand-name {
    font-weight: 500;
    font-size: 20px;
    letter-spacing: 0.5px;
    color: var(--brand-green);
  }
  .brand-tagline {
    margin-top: 6px;
    font-weight: 300;
    font-size: 9px;
    color: var(--brand-green);
  }
  .footer {
    position: absolute;
    left: 0;
    top: 909px;
    width: 100%;
    text-align: center;
    color: var(--ink-body);
    font-weight: 300;
    font-size: 12.5px;
    line-height: 20px;
  }
  .footer-rule {
    width: 455px;
    height: 1px;
    background: var(--rule);
    margin: 0 auto 8px;
  }
  .sep { padding: 0 8px; }
</style>
</head>
<body>
  <main class="letterhead">
    <header class="brand">
      <div class="brand-mark"></div>
      <div class="brand-name">Ferncove Legal</div>
      <div class="brand-tagline">by Attorney M. Calloway</div>
    </header>
    <footer class="footer">
      <div class="footer-rule"></div>
      <p class="footer-addresses">418 Alder Row, Suite #1500 Marston, Georgia 30999<span class="sep">|</span>7215 Linden Ave. Westbrook, Georgia 30998</p>
      <p class="footer-contact">phone: 555-013-8274<span class="sep">|</span>web: https://ferncoveadvice.example</p>
    </footer>
  </main>
</body>
</html>
```